PowerPoint presentation in support of a $6 million capital raise for the acquisition of a business

I need a combination logo design and PowerPoint presentation design. The company name is Brevant Capital Partners, LLC. I have populated the PowerPoint with most of the information, but it's ugly and crowded. I want it to sizzle and look very professional.

I will need to provide additional content, including financial information, during the task. It is not quite finished.

Target Market(s)

sophisticated investors

Industry/Entity Type

Financial

```html
<!DOCTYPE html>
<html lang="en">
<head>
<meta charset="utf-8">
<title>Brevant Capital Partners – Presentation Design</title>
<link href="https://fonts.googleapis.com/css2?family=Roboto:wght@300;400;500;700&family=Roboto+Condensed:wght@400;700&display=swap" rel="stylesheet">
<style>
:root{
  --bg:#232323;
  --orange:#d0891f;
  --ink:#1f1f1f;
  --body:#555;
  --muted:#8a8a8a;
  --rule:#4a4a4a;
  --slide-top:#f3f3f3;
  --slide-bot:#e1e1e1;
  --band:#2d3136;
  --teal:#3db39e;
  --green:#6fbf4a;
  --lime:#a6c93a;
  --purple:#7a64a6;
  --cyan:#3aa3bf;
  --slate:#6e7c99;
  --rose:#c46b84;
  --salmon:#dd906c;
  --map-sea:#6fd0f0;
  --map-olive:#9aa31a;
  --map-pale:#cdeeb0;
}
*{margin:0;padding:0;box-sizing:border-box}
html,body{width:1200px;height:1200px;overflow:hidden;background:var(--bg)}
body{position:relative;font-family:"Roboto",sans-serif;color:var(--ink)}

.brand-header{position:absolute;left:0;top:0;width:1200px;text-align:center}
.brand-name{position:absolute;top:158px;left:0;width:1200px;font:400 20px/1 "Roboto",sans-serif;letter-spacing:2px;color:#fff}
.brand-name .mark{display:inline-block;width:16px;height:16px;background:var(--orange);margin-right:10px;vertical-align:-1px}
.brand-tag{position:absolute;top:183px;left:415px;width:375px;display:flex;align-items:center;gap:16px;color:var(--muted);font:400 15px/1 "Roboto",sans-serif;white-space:nowrap}
.brand-tag::before,.brand-tag::after{content:"";flex:1;height:1px;background:var(--rule)}

.slide{position:absolute;width:380px;height:238px;background:linear-gradient(180deg,var(--slide-top),var(--slide-bot));overflow:hidden;font-family:"Roboto",sans-serif}
.s-logo{position:absolute;left:40px;top:9px;text-align:center}
.s-logo .nm{font:500 7px/1 "Roboto",sans-serif;color:#444;letter-spacing:.6px}
.s-logo .tg{font:400 3px/1 "Roboto",sans-serif;color:#999;margin-top:2px;border-top:.5px solid #bbb;padding-top:1.5px}
.page-no{position:absolute;left:336px;top:9px;width:14px;height:11px;border-radius:2px;background:var(--orange);color:#fff;font:700 4.5px/11px "Roboto",sans-serif;text-align:center}
.s-foot{position:absolute;left:0;width:100%;bottom:9px;text-align:center;font:400 3.5px/1 "Roboto",sans-serif;color:#aaa}
.s-deco{position:absolute;left:10px;bottom:0;width:56px;height:66px;background:linear-gradient(135deg,rgba(190,190,190,0),rgba(180,180,180,.45))}
.s-title{position:absolute;left:36px;top:46px;font:700 8px/1 "Roboto Condensed",sans-serif;color:var(--ink)}
.s-title .hl{color:var(--orange)}
.txt{font:400 3.8px/1.55 "Roboto",sans-serif;color:var(--body)}

.photo{background:linear-gradient(160deg,#c9d3dc,#8a9aa6 55%,#5d6a72)}

.s-welcome{background:linear-gradient(135deg,#eef3f6,#dfe8ee)}
.s-welcome .mark-name{position:absolute;left:64px;top:104px;width:100px;text-align:center;font:500 9px/1 "Roboto",sans-serif;color:#333;letter-spacing:.5px}
.s-welcome .mark-tag{position:absolute;left:64px;top:118px;width:100px;text-align:center;font:400 3.2px/1 "Roboto",sans-serif;color:#999;border-top:.5px solid #bbb;padding-top:2px}
.s-welcome .divider{position:absolute;left:172px;top:55px;width:2px;height:130px;background:linear-gradient(180deg,transparent,rgba(255,255,255,.9),transparent);box-shadow:2px 0 4px rgba(0,0,0,.05)}
.s-welcome .hello{position:absolute;left:193px;top:84px;font:300 8.5px/1 "Roboto",sans-serif;color:#9a9a9a}
.s-welcome .headline{position:absolute;left:193px;top:97px;font:700 13.5px/1.25 "Roboto Condensed",sans-serif;color:var(--orange)}
.s-welcome .date{position:absolute;left:193px;top:143px;font:400 4.5px/1.35 "Roboto",sans-serif;color:#888}
.s-welcome .date b{color:#333;font-weight:500}

.overview-band{position:absolute;left:0;top:50px;width:100%;height:44px;background:var(--band)}
.overview-band .photo{position:absolute;left:0;top:0;width:134px;height:44px;background:linear-gradient(120deg,#1f3f6e,#5f86b5 50%,#d9dde2)}
.overview-band h3{position:absolute;left:141px;top:5px;font:400 7px/1 "Roboto Condensed",sans-serif;color:#fff}
.overview-band h3 span{color:var(--orange)}
.overview-band .txt{position:absolute;left:141px;top:16px;width:214px;color:#c8c8c8;font-size:3.4px}
.s-body{position:absolute;left:41px;width:300px}

.dot-list{list-style:none}
.dot-list li{position:relative;padding-left:12px;margin-bottom:6px}
.dot-list li::before{content:"";position:absolute;left:0;top:1.5px;width:2.5px;height:2.5px;border-radius:50%;background:var(--orange)}
.arrow-list{list-style:none}
.arrow-list li{position:relative;padding-left:15px;margin-bottom:8px}
.arrow-list li svg{position:absolute;left:0;top:2px}

.store-card{position:absolute;width:100px;height:100px;border:1.5px solid var(--orange);background:var(--orange)}
.store-card .photo{width:100%;height:86px}
.store-card .cap{font:400 3.8px/12px "Roboto",sans-serif;color:#fff;text-align:center}
.s-sub{position:absolute;left:0;width:100%;text-align:center;font:400 4.5px/1 "Roboto",sans-serif;color:#555}

.map{position:absolute;left:78px;top:62px;width:232px;height:136px;background:linear-gradient(100deg,var(--map-olive) 0%,#b3bb3a 40%,var(--map-pale) 70%,var(--map-sea) 100%)}
.legend{position:absolute;left:78px;top:205px;display:flex;gap:12px;font:400 3.6px/7px "Roboto",sans-serif;color:#444}
.legend i{display:inline-block;width:7px;height:7px;margin-right:4px;vertical-align:top}

.node{position:absolute;width:59px;height:19px;color:#fff;text-align:center;padding-top:2.5px}
.node b{display:block;font:400 6px/1 "Roboto Condensed",sans-serif}
.node small{display:block;font:400 3.8px/1.2 "Roboto",sans-serif;opacity:.9}
.node.solo{padding-top:6px}

.tile{position:absolute;width:79px;height:59px;border:1.2px solid var(--orange);background:var(--orange)}
.tile .photo{width:100%;height:48px}
.tile .cap{font:400 3.4px/9px "Roboto",sans-serif;color:#fff;text-align:center}

.credit{position:absolute;top:1122px;left:0;width:1200px;text-align:center;font:400 11px/1 "Roboto Condensed",sans-serif;color:#fff;letter-spacing:.2px}
</style>
</head>
<body>

<header class="brand-header">
  <div class="brand-name"><span class="mark"></span>BREVANT CAPITAL PARTNERS</div>
  <div class="brand-tag">Your Business Tagline Here</div>
</header>

<section class="slide s-welcome" style="left:14px;top:274px">
  <div class="mark-name">BREVANT CAPITAL</div>
  <div class="mark-tag">Your Business Tagline Here</div>
  <div class="divider"></div>
  <div class="hello">WELCOME</div>
  <div class="headline">Summary Business Plan<br>Presentation</div>
  <div class="date">November 1, 2013<br>Presented By <b>Daniel Holloway</b></div>
</section>

<section class="slide" style="left:410px;top:274px">
  <div class="s-logo"><div class="nm">BREVANT CAPITAL</div><div class="tg">Your Business Tagline Here</div></div>
  <div class="page-no">2</div>
  <div class="overview-band">
    <div class="photo" role="img" aria-label="Photo of hands reviewing financial documents with a pen and calculator"></div>
    <h3>COMPANY <span>OVERVIEW</span></h3>
    <p class="txt">Brevant Capital Partners, LLC (BCP) was formed by R. Dane Holloway for the purpose of acquiring and operating financial services companies in the small-dollar consumer lending industry. Mr. Holloway has both extensive operating experience in banking and financial service environments and strong academic credentials in this industry.</p>
  </div>
  <div class="s-body txt" style="top:111px">
    <p style="margin-bottom:5px">Mr. Holloway received his Bachelor degree in Investments and Investor Psychology and his Master of Science degree in Banking and Financial Services. He was a founding shareholder of two regional banks and served as Chairman of the Board of a community bank. He founded and operated two advisory firms, both of which provided investment advisory services to high net worth and institutional investors and performed due diligence on complex financial instruments.</p>
    <p>A prior holding company he led included wealth management, private equity and hedge fund management units. This experience operating financial services businesses and evaluating credit in wealth management and banking environments provides him with a unique and informed perspective for acquiring, operating, and growing a consumer lending business.</p>
  </div>
  <div class="s-deco" role="img" aria-label="Faint decorative square pattern"></div>
  <div class="s-foot">Brevant Capital Partners, LLC</div>
</section>

<section class="slide" style="left:806px;top:274px">
  <div class="s-logo"><div class="nm">BREVANT CAPITAL</div><div class="tg">Your Business Tagline Here</div></div>
  <div class="page-no">3</div>
  <div class="s-title">The Title Loan Business Model</div>
  <div class="s-body txt" style="left:36px;top:64px;width:310px">
    <p style="margin-bottom:5px">The small-credit loan industry in the U.S. is comprised of payday lenders (aka check advance), and title loan lenders. Industry associations estimate 1 million consumers obtain title loans worth <b>$6 billion</b> annually, and payday loan volume at <b>$38 billion</b> annually. The small-credit loan industry is part of the larger U.S. consumer credit market. According to the Federal Reserve total U.S. consumer credit outstanding is <b>$3,027 billion</b>. Accordingly, the small-credit loan industry represents less than 1.5% of the total.</p>
    <p style="margin-bottom:5px">There are an estimated 23,000 payday loan stores nationwide. These stores make small (typically less than $300), short-term (2 week), unsecured loans. Lenders verify employment and collect a post-dated check in the full amount of the loan plus fees. Regulation of payday lenders varies widely by jurisdiction, and loan APRs are typically very high.</p>
    <p style="margin-bottom:6px">There are an estimated 15,000 title loan shops in the U.S. These shops make short-term (26 week) loans averaging $950 equal to 20 – 60% of the value of the borrower's automobile. The loans are secured by a lien on their car title. Regulation of title lenders also varies widely by jurisdiction. A typical title loan would be made at an APR of 240% – 20% per month. Lenders will hold the physical car title and a spare key and repossess the car in the event of default, with accrued interest paid upon sale.</p>
    <p style="font:700 4.6px/1.4 'Roboto',sans-serif;color:#333">The historical default rate for both payday and title loans has averaged <span style="color:var(--orange)">6% of loans – roughly 20%</span> of gross revenue.</p>
  </div>
  <div class="s-deco" role="img" aria-label="Faint decorative square pattern"></div>
  <div class="s-foot">Brevant Capital Partners, LLC</div>
</section>

<section class="slide" style="left:14px;top:539px">
  <div class="s-logo"><div class="nm">BREVANT CAPITAL</div><div class="tg">Your Business Tagline Here</div></div>
  <div class="page-no">4</div>
  <div class="s-title">The Title Loan Business Model</div>
  <div class="s-body txt" style="left:36px;top:64px;width:300px">
    <p style="margin-bottom:7px;font-size:4.6px;color:#333">The title loan business model operates (generally) as follows:</p>
    <ul class="dot-list" style="padding-left:14px">
      <li>Loans averaging $950 equal to 20% to 60% of the auction (liquidation) value of the borrowers auto are made at rates averaging 20% per month for an average duration of approximately 6 months.</li>
      <li>The lender takes the borrower through a process to verify ownership and a clean title, photograph the automobile, determine value, secure the physical title, obtain a spare ignition key and gather appropriate information regarding the borrower.</li>
      <li>The borrower makes monthly payments pursuant to the terms of the loan; if the borrower fails to pay the loan as required, the lender will move to repossess the collateral and liquidate it to satisfy the loan amount plus interest and fees.</li>
      <li>Bad loans average 6% of total loans and 20% of gross revenues.</li>
      <li>Gross profit of 80% and net income (before taxes) of 40% is typical for a mature, well run title loan business.</li>
    </ul>
  </div>
  <div class="s-deco" role="img" aria-label="Faint decorative square pattern"></div>
  <div class="s-foot">Brevant Capital Partners, LLC</div>
</section>

<section class="slide" style="left:410px;top:539px">
  <div class="s-logo"><div class="nm">BREVANT CAPITAL</div><div class="tg">Your Business Tagline Here</div></div>
  <div class="page-no">5</div>
  <div class="s-title">The Title Loan Industry's Largest Operators</div>
  <div class="s-body txt" style="left:36px;top:71px;width:310px;font-size:4.2px;color:#444">
    <p style="margin-bottom:10px">With estimated annual loan volume of $6 billion, the title loan industry does not attract large corporate operators. The notable exceptions are AutoTitle Plus and LoanCrest. The following are some of the title loan industry's largest operators:</p>
    <ul class="arrow-list txt" style="padding-left:0">
      <li><svg width="5" height="8" viewBox="0 0 5 8"><path d="M1 1l3 3-3 3" fill="none" stroke="#d0891f" stroke-width="1.2"/></svg>AutoTitle Plus operates more than 1,200 stores spanning 12 states across the South, Midwest and Southwest. With an average title loan portfolio of $300,000 per store, it is estimated to have an aggregate loan portfolio in excess of $300 million. This represents a market share of 5%.</li>
      <li><svg width="5" height="8" viewBox="0 0 5 8"><path d="M1 1l3 3-3 3" fill="none" stroke="#d0891f" stroke-width="1.2"/></svg>LoanCrest, founded in 1990, operates more than 900 stores in approximately 20 states, with a concentration in the Southwest and Southeast.</li>
      <li><svg width="5" height="8" viewBox="0 0 5 8"><path d="M1 1l3 3-3 3" fill="none" stroke="#d0891f" stroke-width="1.2"/></svg>A number of other operators offer multiple product lines including title loans, payday loans, and/or tax preparation.</li>
    </ul>
  </div>
  <div class="s-deco" role="img" aria-label="Faint decorative square pattern"></div>
  <div class="s-foot">Brevant Capital Partners, LLC</div>
</section>

<section class="slide" style="left:806px;top:539px">
  <div class="s-logo"><div class="nm">BREVANT CAPITAL</div><div class="tg">Your Business Tagline Here</div></div>
  <div class="page-no">6</div>
  <div class="s-title">The Title Loan Industry's Largest Operators</div>
  <div class="s-sub" style="top:73px">Sample of Store</div>
  <div class="store-card" style="left:78px;top:90px">
    <div class="photo" role="img" aria-label="Photo of a title loan storefront with a red sign"></div>
    <div class="cap">AutoTitle Plus Store</div>
  </div>
  <div class="store-card" style="left:210px;top:90px">
    <div class="photo" role="img" aria-label="Photo of a loan store building with red awnings and a parked car" style="background:linear-gradient(170deg,#4f8fd6,#a7c4e0 40%,#a5675a 65%,#7a7a7a)"></div>
    <div class="cap">LoanCrest Store</div>
  </div>
  <div class="s-deco" role="img" aria-label="Faint decorative square pattern"></div>
  <div class="s-foot">Brevant Capital Partners, LLC</div>
</section>

<section class="slide" style="left:14px;top:804px">
  <div class="s-logo"><div class="nm">BREVANT CAPITAL</div><div class="tg">Your Business Tagline Here</div></div>
  <div class="page-no">10</div>
  <div class="s-title">Presence of Car Title Lending by State and Maximum APR</div>
  <div class="map" role="img" aria-label="Map of the United States showing which states have car title lending and each state's maximum APR"></div>
  <div class="legend">
    <span><i style="background:var(--map-olive)"></i>States with Car Title Lending</span>
    <span><i style="background:var(--map-pale)"></i>States without Car Title Lending</span>
  </div>
  <div class="s-deco" role="img" aria-label="Faint decorative square pattern"></div>
  <div class="s-foot">Brevant Capital Partners, LLC</div>
</section>

<section class="slide" style="left:410px;top:804px">
  <div class="s-logo"><div class="nm">BREVANT CAPITAL</div><div class="tg">Your Business Tagline Here</div></div>
  <div class="page-no">20</div>
  <svg width="380" height="238" style="position:absolute;left:0;top:0" aria-hidden="true">
    <g fill="none" stroke="#777" stroke-width=".6" stroke-dasharray="1 1">
      <path d="M186 66 L144 88"/>
      <path d="M244 66 L292 88"/>
      <path d="M112 100 L88 113"/>
      <path d="M144 100 L168 113"/>
    </g>
  </svg>
  <div class="node" style="left:186px;top:53px;height:20px;background:var(--teal)"><b>R. Dane Holloway</b><small>Chairman &amp; CEO</small></div>
  <div class="node" style="left:112px;top:88px;width:32px;height:18px;background:var(--green)"><b>TBD</b><small>COO</small></div>
  <div class="node" style="left:57px;top:118px;background:var(--lime)"><b>Nora Whitfield</b><small>Regional Manager</small></div>
  <div class="node" style="left:140px;top:118px;background:var(--lime)"><b>Grant Melner</b><small>Collection Manager</small></div>
  <div class="node solo" style="left:57px;top:145px;background:var(--purple)"><b>Store Manager</b></div>
  <div class="node" style="left:140px;top:145px;background:var(--cyan)"><b>Tessa Corwin</b><small>Head Underwriter</small></div>
  <div class="node" style="left:57px;top:170px;height:20px;background:var(--purple)"><b>Store Manager<br>Assistant</b></div>
  <div class="node" style="left:140px;top:170px;background:var(--slate)"><b>Evan Pryor</b><small>Head IT</small></div>
  <div class="node" style="left:262px;top:92px;background:var(--rose)"><b>Owen Haskell</b><small>CFO</small></div>
  <div class="node" style="left:262px;top:118px;background:var(--salmon)"><b>Laura Keene</b><small>Assistant Accountant</small></div>
  <div class="s-deco" role="img" aria-label="Faint decorative square pattern"></div>
  <div class="s-foot">Brevant Capital Partners, LLC</div>
</section>

<section class="slide" style="left:806px;top:804px">
  <div class="s-logo"><div class="nm">BREVANT CAPITAL</div><div class="tg">Your Business Tagline Here</div></div>
  <div class="page-no">13</div>
  <div class="s-title">The Initial Opportunity: <span class="hl">Cash Rail, LLC</span></div>
  <div class="tile" style="left:49px;top:67px"><div class="photo" role="img" aria-label="Photo of a Cash Rail storefront"></div><div class="cap">Nampa, Idaho</div></div>
  <div class="tile" style="left:150px;top:67px"><div class="photo" role="img" aria-label="Photo of a Cash Rail storefront" style="background:linear-gradient(170deg,#9ab8d8,#c59a86 55%,#7d6e66)"></div><div class="cap">Idaho Falls, Idaho</div></div>
  <div class="tile" style="left:252px;top:67px"><div class="photo" role="img" aria-label="Photo of a Cash Rail storefront" style="background:linear-gradient(170deg,#6a86a8,#4b5a4c 55%,#3c3c3c)"></div><div class="cap">Clearfield, Utah</div></div>
  <div class="tile" style="left:49px;top:138px"><div class="photo" role="img" aria-label="Photo of a Cash Rail storefront" style="background:linear-gradient(170deg,#7fa7d4,#a4443f 55%,#6f6a66)"></div><div class="cap">Boise, Idaho</div></div>
  <div class="tile" style="left:150px;top:138px"><div class="photo" role="img" aria-label="Photo of a Cash Rail storefront" style="background:linear-gradient(170deg,#b8c4cc,#8a7a62 55%,#6b6b66)"></div><div class="cap">West Valley, Utah</div></div>
  <div class="tile" style="left:252px;top:138px"><div class="photo" role="img" aria-label="Photo of a Cash Rail storefront" style="background:linear-gradient(170deg,#5f8fc8,#9a6a4e 55%,#6a625c)"></div><div class="cap">Las Cruces, New Mexico</div></div>
  <div class="s-deco" role="img" aria-label="Faint decorative square pattern"></div>
  <div class="s-foot">Brevant Capital Partners, LLC</div>
</section>

<div class="credit">POWER POINT PRESENTATION</div>

</body>
</html>
```